High End Business Card Design for Flooring Store

Looking for a new card design for our hardwood flooring company. We have no print budget for these and are open to cards made from wood, metal, cardstock with embossed print ... or any combination of these. No plastic.

We sell luxury products and I want the cards to reflect our image of quality and class.

Our contact information as such;
Employee Name
418 Colbrook Blvd.
Harwick, ON
K9R-3M5
(555) 214-3968
Employee email @velkaflooring.com

Target Market(s)

Home Builders

Contact Information for Business Card

Emnployee name, business contact information

```html
<!DOCTYPE html>
<html lang="en">
<head>
<meta charset="utf-8">
<title>Velka Flooring – Business Card</title>
<link rel="stylesheet" href="https://fonts.googleapis.com/css2?family=Open+Sans:wght@400;600;700&display=swap">
<style>
  :root {
    --page: #2e2f31;
    --card: #eef0f1;
    --card-edge: #dfe3e6;
    --accent-red: #9a2420;
    --ink: #1f1f1f;
    --muted: #4a4a4a;
  }
  * { margin: 0; padding: 0; box-sizing: border-box; }
  html, body { width: 1200px; height: 900px; overflow: hidden; }
  body {
    background: var(--page);
    font-family: "Open Sans", Arial, sans-serif;
    position: relative;
  }
  .card {
    position: absolute;
    left: 290px;
    width: 620px;
    height: 354px;
    background: radial-gradient(ellipse at 40% 30%, #f6f7f8 0%, var(--card) 60%, var(--card-edge) 100%);
    box-shadow: 0 10px 24px rgba(0,0,0,0.45);
  }
  .card--front { top: 70px; }
  .card--back { top: 476px; }

  .brand {
    position: absolute;
    display: flex;
    flex-direction: column;
    align-items: center;
  }
  .brand__name {
    font-weight: 600;
    color: var(--ink);
    font-size: 64px;
    line-height: 1.05;
    letter-spacing: 2px;
  }
  .brand__tagline {
    margin-top: 6px;
    font-size: 14px;
    letter-spacing: 1.5px;
    text-transform: uppercase;
    color: var(--muted);
  }
  .card--front .brand { left: 0; right: 0; top: 112px; }
  .card--back .brand { right: 40px; top: 36px; align-items: flex-end; }

  .divider {
    position: absolute;
    left: 168px;
    right: 28px;
    top: 212px;
    height: 1px;
    background: var(--accent-red);
    opacity: 0.8;
  }
  .person { position: absolute; left: 40px; top: 178px; }
  .person__name { font-weight: 700; font-size: 17px; color: var(--ink); letter-spacing: 0.3px; }
  .person__role { font-size: 15px; color: var(--accent-red); }

  .contact {
    position: absolute;
    left: 40px;
    top: 258px;
    list-style: none;
    font-size: 15px;
    color: var(--muted);
  }
  .contact__item { display: flex; align-items: center; gap: 10px; height: 26px; }
  .contact__icon { width: 14px; height: 14px; fill: var(--ink); flex: none; }
</style>
</head>
<body>

<section class="card card--front" aria-label="Card front">
  <div class="brand">
    <span class="brand__name">Velka</span>
    <p class="brand__tagline">Hardwood Flooring · Stairs</p>
  </div>
</section>

<section class="card card--back" aria-label="Card back">
  <div class="brand">
    <span class="brand__name">Velka</span>
    <p class="brand__tagline">Hardwood Flooring · Stairs</p>
  </div>

  <div class="person">
    <p class="person__name">ALEX MORIN</p>
    <p class="person__role">Manager</p>
  </div>
  <div class="divider"></div>

  <ul class="contact">
    <li class="contact__item">
      <svg class="contact__icon" viewBox="0 0 24 24" aria-hidden="true"><path d="M6.6 10.8a15 15 0 0 0 6.6 6.6l2.2-2.2a1 1 0 0 1 1-.25 11.4 11.4 0 0 0 3.6.6 1 1 0 0 1 1 1V20a1 1 0 0 1-1 1A17 17 0 0 1 3 4a1 1 0 0 1 1-1h3.5a1 1 0 0 1 1 1c0 1.25.2 2.45.6 3.6a1 1 0 0 1-.25 1z"/></svg>
      <span>(555) 214-3968</span>
    </li>
    <li class="contact__item">
      <svg class="contact__icon" viewBox="0 0 24 24" aria-hidden="true"><path d="M2 5h20v14H2z M4 7v.5l8 5.5 8-5.5V7z" fill-rule="evenodd"/></svg>
      <span>alex@velkaflooring.com</span>
    </li>
    <li class="contact__item">
      <svg class="contact__icon" viewBox="0 0 24 24" aria-hidden="true"><path d="M12 2a7 7 0 0 0-7 7c0 5 7 13 7 13s7-8 7-13a7 7 0 0 0-7-7zm0 9.5A2.5 2.5 0 1 1 12 6.5a2.5 2.5 0 0 1 0 5z"/></svg>
      <span>418 Colbrook Blvd., Harwick, ON, K9R-3M5</span>
    </li>
  </ul>
</section>

</body>
</html>
```